Brusola Card Design Project

Our company,Brusola, is focusing B to B, and people receiving this card are managers or engineers in the handset maker in the world.
Therefore we hope this to be designed strictly serious one but it needs cool and unique style which could imagine something innovation from the card.

This card will be used for Japanese,Chinese and English.
Please consider 2 byte character usage.

It Company

```html
<!DOCTYPE html>
<html lang="en">
<head>
<meta charset="utf-8">
<title>Brusola Business Cards</title>
<link href="https://fonts.googleapis.com/css2?family=Questrial&display=swap" rel="stylesheet">
<style>
  :root {
    --stage-light: #f2f2f2;
    --stage-dark: #b9b9b9;
    --card-white: #ffffff;
    --card-mist: #e4e4e4;
    --band-light: #b4b4b4;
    --band-dark: #7d7d7d;
    --ink: #555555;
    --ink-soft: #3c3c3c;
    --ink-faint: #b0b0b0;
    --back-base: #c9c9c9;
    --back-deep: #5e5e5e;
    --brand-grey: #6e6e6e;
  }
  * { margin: 0; padding: 0; box-sizing: border-box; }
  html, body { width: 1200px; height: 1200px; overflow: hidden; }
  body {
    background: radial-gradient(circle at 50% 45%, var(--stage-light) 0%, #dcdcdc 60%, var(--stage-dark) 100%);
    font-family: "Questrial", "Century Gothic", sans-serif;
    position: relative;
  }
  .card {
    position: absolute;
    width: 620px;
    height: 350px;
    overflow: hidden;
    box-shadow: 0 14px 30px rgba(0,0,0,0.28);
  }

  /* Front */
  .card-front {
    left: 110px; top: 130px;
    background: radial-gradient(circle at 55% 35%, var(--card-white) 0%, var(--card-mist) 90%);
  }
  .front-brand {
    position: absolute; left: 60px; top: 170px;
    display: flex; align-items: center; gap: 12px;
  }
  .brand-square { width: 18px; height: 18px; background: var(--brand-grey); }
  .brand-name {
    font-size: 34px; color: var(--brand-grey); letter-spacing: 1px;
  }
  .holder { position: absolute; left: 310px; top: 50px; }
  .holder-name { font-size: 36px; color: var(--ink); line-height: 1; }
  .holder-position {
    font-size: 15px; color: var(--ink-faint); text-align: right; margin-top: -2px;
  }
  .contact {
    position: absolute; left: 310px; top: 130px;
    font-size: 15px; color: var(--ink-soft); line-height: 19px; list-style: none;
  }
  .contact li { display: flex; align-items: center; gap: 8px; }
  .contact svg { width: 14px; height: 12px; fill: var(--ink-soft); flex: none; }
  .band-right {
    position: absolute; left: 240px; right: 0; top: 250px; bottom: 0;
    background: var(--band-light);
  }
  .band-left {
    position: absolute; left: 0; width: 290px; top: 284px; bottom: 0;
    background: var(--band-dark);
  }
  .band-step {
    position: absolute; left: 240px; width: 50px; top: 250px; height: 34px;
    background: var(--band-dark);
  }

  /* Back */
  .card-back {
    left: 470px; top: 640px;
    background: linear-gradient(160deg, #d6d6d6 0%, var(--back-base) 60%, #bdbdbd 100%);
  }
  .back-feature {
    position: absolute; right: 0; top: 0; width: 230px; height: 100%;
    background: linear-gradient(200deg, var(--back-deep) 0%, #8a8a8a 55%, #a8a8a8 100%);
  }
  .back-brand {
    position: absolute; left: 44px; top: 112px;
    font-size: 96px; color: var(--brand-grey); letter-spacing: 2px; line-height: 1;
  }
  .back-web {
    position: absolute; left: 66px; top: 222px;
    font-size: 21px; color: #4a4a4a; letter-spacing: 2.5px;
  }
</style>
</head>
<body>

<section class="card card-front" aria-label="Business card front">
  <div class="front-brand">
    <span class="brand-square"></span>
    <span class="brand-name">BRUSOLA</span>
  </div>
  <div class="holder">
    <div class="holder-name">Business Name</div>
    <div class="holder-position">Position</div>
  </div>
  <ul class="contact">
    <li>18 Unit/4 Harbor Lane,</li>
    <li>456, NY</li>
    <li><svg viewBox="0 0 14 12" aria-hidden="true"><path d="M1 4 Q7 -1 13 4 L11 5.5 L9.5 4 L4.5 4 L3 5.5 Z M3 6 H11 V11 H3 Z"/></svg>0425 310482</li>
    <li><svg viewBox="0 0 14 12" aria-hidden="true"><path d="M1 2 H13 V11 H1 Z M1 2 L7 7 L13 2" stroke="#fff" stroke-width="1"/></svg>brusolaofficial@email.com</li>
    <li><svg viewBox="0 0 14 12" aria-hidden="true"><circle cx="7" cy="6" r="5" fill="none" stroke="#3c3c3c" stroke-width="2"/><rect x="3" y="5" width="8" height="2"/></svg>www.brusola.com</li>
  </ul>
  <div class="band-right"></div>
  <div class="band-step"></div>
  <div class="band-left"></div>
</section>

<section class="card card-back" aria-label="Business card back">
  <div class="back-feature" role="img" aria-label="Large decorative graphic area in deep grey tones"></div>
  <div class="back-brand">BRUSOLA</div>
  <div class="back-web">www.yourwebsitelink.com</div>
</section>

</body>
</html>
```